High Quality Business card for Property Management Agency - Super Classy and professional design

High Quality Business card design.

We need a business card designed for our Property Management Agency.
We are located on Sydney's Northern Beaches and manage beautiful properties along the beach and harbor.
We need a design that oozes modern, classy and professional.
I would like it to be double sided with contact details and logo on the front and just the logo on the back.

I need a print ready PDF version of the file as well as an editable photoshop (PSD) version of the file.

Logo and information details attached.

Target Market(s)

Property owners/investors, Male and Female Aged 28-65

Industry/Entity Type

Real Estate

Contact Information for Business Card

Tom Harlow
Tel: 0437 216 590
Email: tom@harlowestates.com.au
Website: www.harlowestates.com.au
Address: Level 2, 17 Kestrel Rd, Wendale NSW 2081

Font styles to use
Sans Serif

Requirements
Must have
• - Logo front and back
• - Business card details listed above and attached
• - Colour
Nice to have
• Sleek and professional

```html
<!DOCTYPE html>
<html lang="en">
<head>
<meta charset="utf-8">
<title>Harlow Estates – Business Card</title>
<link href="https://fonts.googleapis.com/css2?family=Nunito+Sans:wght@300;400;700&display=swap" rel="stylesheet">
<style>
  :root {
    --backdrop: #e9e7e3;
    --card-front: #939a96;
    --card-back: #7c8381;
    --card-back-light: #8d9391;
    --teal: #1a9a9c;
    --text-light: #eef0ee;
    --text-soft: #e2e6e3;
    --white: #ffffff;
  }
  * { margin: 0; padding: 0; box-sizing: border-box; }
  html, body {
    width: 1200px;
    height: 867px;
    overflow: hidden;
    background: var(--backdrop);
    font-family: "Nunito Sans", sans-serif;
  }
  .sheet {
    position: relative;
    width: 1200px;
    height: 867px;
    display: flex;
    align-items: center;
    justify-content: center;
    gap: 48px;
  }
  .card {
    position: relative;
    width: 500px;
    height: 306px;
    border-radius: 3px;
    overflow: hidden;
    box-shadow: 0 10px 28px rgba(0,0,0,0.18);
  }

  /* Contact side */
  .card--contact {
    background: var(--card-front);
    color: var(--text-soft);
  }
  .card--contact .edge-band {
    position: absolute;
    top: 0; right: 0;
    width: 10px; height: 100%;
    background: var(--teal);
  }
  .holder-name {
    position: absolute;
    left: 56px; top: 62px;
    font-weight: 300;
    font-size: 38px;
    letter-spacing: 0.5px;
    color: var(--text-light);
  }
  .contact-list {
    position: absolute;
    left: 62px; top: 148px;
    list-style: none;
  }
  .contact-list li {
    display: flex;
    align-items: center;
    gap: 12px;
    height: 26px;
    font-weight: 300;
    font-size: 13px;
    letter-spacing: 0.3px;
  }
  .contact-icon {
    width: 16px; height: 16px;
    flex: none;
  }

  /* Brand side */
  .card--brand {
    background: var(--card-back);
    display: flex;
    align-items: center;
    justify-content: center;
  }
  .brand-texture {
    position: absolute;
    inset: 0;
    background:
      linear-gradient(135deg, var(--card-back-light) 0%, var(--card-back) 45%, var(--card-back-light) 70%, var(--card-back) 100%);
  }
  .brand-name {
    position: relative;
    font-weight: 700;
    font-size: 40px;
    letter-spacing: 1px;
    color: var(--white);
    text-transform: uppercase;
  }
</style>
</head>
<body>
<main class="sheet">

  <section class="card card--contact">
    <h1 class="holder-name">Tom Harlow</h1>
    <ul class="contact-list">
      <li>
        <svg class="contact-icon" viewBox="0 0 16 16" fill="none" stroke="currentColor" stroke-width="1">
          <circle cx="8" cy="8" r="7.3"/>
          <path d="M5.6 4.6l1.3 1.6-.7 1c.5 1 1.3 1.8 2.3 2.3l1-.7 1.6 1.3-.8 1.1c-2.6-.4-4.7-2.5-5.1-5.1z"/>
        </svg>
        0437 216 590
      </li>
      <li>
        <svg class="contact-icon" viewBox="0 0 16 16" fill="none" stroke="currentColor" stroke-width="1">
          <circle cx="8" cy="8" r="7.3"/>
          <rect x="4.5" y="5.5" width="7" height="5" rx="0.5"/>
          <path d="M4.7 5.8L8 8.4l3.3-2.6"/>
        </svg>
        tom@harlowestates.com.au
      </li>
      <li>
        <svg class="contact-icon" viewBox="0 0 16 16" fill="none" stroke="currentColor" stroke-width="1">
          <circle cx="8" cy="8" r="7.3"/>
          <circle cx="8" cy="8" r="3.6"/>
          <path d="M4.4 8h7.2M8 4.4c-1.2 1.2-1.2 6 0 7.2M8 4.4c1.2 1.2 1.2 6 0 7.2"/>
        </svg>
        www.harlowestates.com.au
      </li>
      <li>
        <svg class="contact-icon" viewBox="0 0 16 16" fill="none" stroke="currentColor" stroke-width="1">
          <circle cx="8" cy="8" r="7.3"/>
          <path d="M8 12s-3-3.2-3-5.2a3 3 0 016 0C11 8.8 8 12 8 12z"/>
          <circle cx="8" cy="6.8" r="1"/>
        </svg>
        Level 2, 17 Kestrel Rd, Wendale NSW 2081
      </li>
    </ul>
    <div class="edge-band"></div>
  </section>

  <section class="card card--brand">
    <div class="brand-texture" role="img" aria-label="Faint grey geometric triangle background texture"></div>
    <p class="brand-name">Harlow Estates</p>
  </section>

</main>
</body>
</html>
```